Interactive Tailored Suit and Shirt Website Needs Homepage Redesign

We need our homepage redesigned. Our current website is dated and we need a refresh. We are a Melbourne based business selling tailored suits and shirts in store and online. The homepage should be fashion forward. Our colour scheme has traditionally been black and white but would interested in new ideas.
Our current website is quillora.com.au

```html
<!DOCTYPE html>
<html lang="en">
<head>
<meta charset="utf-8">
<title>Quillora — Tailored Suits and Shirts</title>
<link rel="stylesheet" href="https://fonts.googleapis.com/css2?family=Roboto:wght@400;700;900&display=swap">
<style>
:root{
  --orange:#f26522;
  --ink:#2b2b2b;
  --dark:#333333;
  --darker:#262626;
  --grey:#777;
  --line:#dcdcdc;
  --cream:#eeebe4;
  --white:#ffffff;
  --photo-a:#8c8f93;
  --photo-b:#3a3d42;
}
*{box-sizing:border-box;margin:0;padding:0}
html,body{width:811px;height:1200px;overflow:hidden}
body{font-family:"Roboto",Arial,sans-serif;color:var(--ink);background:var(--white);position:relative;font-size:7px}
.abs{position:absolute}
a{color:inherit;text-decoration:none}

/* header */
.site-header{left:0;top:0;width:811px;height:76px;background:var(--white);border-bottom:1px solid var(--line)}
.logo{left:60px;top:12px;font-size:20px;font-weight:700;color:var(--ink);letter-spacing:-.3px}
.utility{right:60px;top:10px;display:flex;gap:14px;font-size:6.5px;color:var(--grey)}
.main-nav{left:60px;top:46px;display:flex;font-size:7.5px}
.main-nav a{padding:7px 14px;color:var(--ink)}
.main-nav a.active{background:var(--orange);color:var(--white)}

/* hero */
.hero{left:0;top:76px;width:811px;height:190px;background:linear-gradient(180deg,#a9abad,#c9cacb 60%,#b3b4b6);overflow:hidden}
.hero-photo{left:390px;top:0;width:240px;height:190px;background:linear-gradient(180deg,#9a9c9f 0%,#6e7175 35%,var(--photo-b) 100%)}
.hero-copy{left:60px;top:30px;width:300px}
.hero-copy h1{font-size:17px;line-height:20px;font-weight:700;color:var(--darker)}
.hero-copy h1 span{color:var(--orange)}
.hero-copy p{margin-top:10px;font-size:7px;line-height:10px;color:#333;width:230px}
.btn{display:inline-block;background:var(--orange);color:var(--white);font-size:6.5px;padding:5px 10px}
.hero-copy .btn{margin-top:18px}
.hero-rule{left:0;top:266px;width:811px;height:4px;background:var(--orange)}

/* featured */
.featured{left:0;top:270px;width:811px;height:110px;background:var(--cream)}
.label-orange{font-size:7.5px;color:var(--orange);font-weight:700}
.featured .title-left{left:60px;top:12px}
.thumbs{left:60px;top:30px;display:flex;gap:10px}
.thumb{width:55px;text-align:center;font-size:5.5px;color:var(--grey)}
.thumb .pic{height:52px;background:linear-gradient(180deg,var(--photo-a),var(--photo-b));margin-bottom:4px}
.brands-title{left:540px;top:12px;font-size:7.5px;font-weight:700;color:var(--ink)}
.brand-box{left:540px;top:30px;width:205px;height:62px;background:var(--orange);color:var(--white);font-size:13px;display:flex;align-items:center;justify-content:center;border:1px solid #ffffff55}

/* listing */
.list-title{left:60px;top:422px;font-size:9px;font-weight:700;color:var(--orange)}
.view-all{left:690px;top:424px;font-size:6px;color:var(--grey)}
.filters{left:60px;top:452px;width:150px}
.select{height:17px;border:1px solid var(--line);margin-bottom:8px;font-size:6px;color:var(--grey);padding:4px 6px;position:relative}
.select:after{content:"";position:absolute;right:6px;top:6px;border:3px solid transparent;border-top-color:var(--grey)}
.filters .btn{margin:4px 0 0 40px}
.side-head{font-size:8.5px;font-weight:700;color:var(--ink);margin:22px 0 8px}
.store{height:34px;background:var(--dark);color:var(--white);padding:8px 10px;margin-bottom:6px;position:relative}
.store b{display:block;font-size:7.5px}
.store span{font-size:5.5px;color:#bbb}
.store i{position:absolute;right:0;top:0;width:16px;height:34px;background:var(--orange)}
.promo{height:62px;background:var(--dark);color:#ccc;font-size:6.5px;display:flex;align-items:center;justify-content:center;text-align:center}

.search{left:300px;top:452px;width:445px;height:17px;border:1px solid var(--line);font-size:6px;color:var(--grey);padding:4px 6px}
.search .go{position:absolute;right:0;top:0;height:15px;width:40px;background:#eee;text-align:center;padding-top:4px}
.grid{left:300px;top:488px;width:445px;display:grid;grid-template-columns:repeat(3,130px);column-gap:27px;row-gap:20px}
.product .pic{height:112px;background:linear-gradient(180deg,#b8b9bb,var(--photo-b));position:relative}
.product .tags{position:absolute;left:0;bottom:0;display:flex}
.product .tags span{font-size:5px;color:var(--white);padding:3px 5px;background:var(--darker)}
.product .tags span.o{background:var(--orange)}
.product h3{margin-top:6px;font-size:7px;color:var(--orange)}
.product p{margin-top:3px;font-size:5.5px;line-height:7.5px;color:var(--grey)}
.pager{left:420px;top:918px;display:flex;gap:4px}
.pager span{width:13px;height:13px;border-radius:50%;border:1px solid var(--line);font-size:6px;text-align:center;line-height:11px;color:var(--grey)}
.pager span.on{background:var(--orange);border-color:var(--orange);color:var(--white)}

/* footer */
.site-footer{left:0;top:965px;width:811px;height:235px;background:var(--dark);color:#bbb}
.foot-col{top:20px}
.foot-col h4{font-size:7.5px;color:var(--orange);margin-bottom:10px}
.foot-col li{list-style:none;font-size:5.5px;line-height:9px}
.cards{display:flex;gap:5px;margin-top:6px}
.cards i{width:24px;height:15px;background:#e6e6e6;border-radius:2px}
.socials{display:flex;gap:6px;margin-top:8px}
.socials i{width:15px;height:15px;border-radius:50%;background:#e6e6e6}
.newsletter{left:520px;top:172px;width:225px;height:18px;display:flex}
.newsletter span{flex:1;background:var(--white);font-size:6px;color:var(--grey);padding:5px 6px}
.newsletter b{width:22px;background:var(--orange)}
.copyright{left:0;top:215px;width:811px;height:20px;background:var(--darker);font-size:5.5px;padding:7px 60px;color:#999}
</style>
</head>
<body>

<header class="abs site-header">
  <div class="abs logo">Quillora</div>
  <div class="abs utility"><a>Sign in</a><a>Order history / Receipt</a><a>Contact us</a><a>Customer help</a></div>
  <nav class="abs main-nav"><a class="active">Home</a><a>About</a><a>Shop ▾</a><a>Add to bag</a></nav>
</header>

<section class="abs hero">
  <div class="abs hero-photo" role="img" aria-label="Model in a tailored grey suit"></div>
  <div class="abs hero-copy">
    <h1>Quillora of <span>Branded suiting for the modern man</span></h1>
    <p>We have suits for all occasions, from the business suit to the dapper special occasion suits to wedding and black tie hire.</p>
    <a class="btn">Learn more</a>
  </div>
</section>
<div class="abs hero-rule"></div>

<section class="abs featured">
  <div class="abs label-orange title-left">Featured Items</div>
  <div class="abs thumbs">
    <div class="thumb"><div class="pic" role="img" aria-label="Featured suit"></div>Item Name</div>
    <div class="thumb"><div class="pic" role="img" aria-label="Featured suit"></div>Item Name</div>
    <div class="thumb"><div class="pic" role="img" aria-label="Featured suit"></div>Item Name</div>
    <div class="thumb"><div class="pic" role="img" aria-label="Featured suit"></div>Item Name</div>
  </div>
  <div class="abs brands-title">Top Selling Brands</div>
  <div class="abs brand-box">BRAND NAME</div>
</section>

<div class="abs list-title">Top Selling Items</div>
<div class="abs view-all">▸ View all items</div>

<aside class="abs filters">
  <div class="select">Select Product Categories</div>
  <div class="select">Search by Size</div>
  <div class="select">Search by Color</div>
  <div class="select">Search by Price</div>
  <a class="btn">Show all items</a>
  <div class="side-head">What's hot</div>
  <div class="store"><b>WOMEN STORE</b><span>New arrivals in</span><i></i></div>
  <div class="store"><b>MEN STORE</b><span>New arrivals in</span><i></i></div>
  <div class="side-head">Promotion</div>
  <div class="promo">300 x 100<br>Promotional Area</div>
</aside>

<div class="abs search">Search products<span class="go">Search</span></div>

<section class="abs grid">
  <article class="product"><div class="pic" role="img" aria-label="Man in a light grey suit"><div class="tags"><span class="o">$299</span><span>Add to bag</span></div></div><h3>Item Name Goes Here</h3><p>Slim fit wool suit with notch lapel, fully lined and tailored.</p></article>
  <article class="product"><div class="pic" role="img" aria-label="Man in a charcoal suit"><div class="tags"><span class="o">$349</span><span>Add to bag</span></div></div><h3>Item Name Goes Here</h3><p>Slim fit wool suit with notch lapel, fully lined and tailored.</p></article>
  <article class="product"><div class="pic" role="img" aria-label="Man in a dark suit"><div class="tags"><span class="o">$399</span><span>Add to bag</span></div></div><h3>Item Name Goes Here</h3><p>Slim fit wool suit with notch lapel, fully lined and tailored.</p></article>
  <article class="product"><div class="pic" role="img" aria-label="Man in a navy suit"><div class="tags"><span class="o">$299</span><span>Add to bag</span></div></div><h3>Item Name Goes Here</h3><p>Slim fit wool suit with notch lapel, fully lined and tailored.</p></article>
  <article class="product"><div class="pic" role="img" aria-label="Man in a black suit"><div class="tags"><span class="o">$349</span><span>Add to bag</span></div></div><h3>Item Name Goes Here</h3><p>Slim fit wool suit with notch lapel, fully lined and tailored.</p></article>
  <article class="product"><div class="pic" role="img" aria-label="Man in a pinstripe suit"><div class="tags"><span class="o">$399</span><span>Add to bag</span></div></div><h3>Item Name Goes Here</h3><p>Slim fit wool suit with notch lapel, fully lined and tailored.</p></article>
</section>

<div class="abs pager"><span>‹</span><span>1</span><span class="on">2</span><span>3</span><span>›</span></div>

<footer class="abs site-footer">
  <div class="abs foot-col" style="left:60px">
    <h4>WE ACCEPT</h4>
    <div class="cards"><i></i><i></i><i></i><i></i></div>
    <h4 style="margin-top:38px">Get Touch</h4>
    <div class="socials"><i></i><i></i><i></i><i></i><i></i></div>
  </div>
  <div class="abs foot-col" style="left:290px">
    <h4>COMPANY</h4>
    <ul><li>Home</li><li>About us</li><li>Contact us</li><li>Our story</li><li>Careers</li><li>Store locator</li><li>Press</li></ul>
  </div>
  <div class="abs foot-col" style="left:450px">
    <h4>SERVICES</h4>
    <ul><li>Suit tailoring</li><li>Shirt fitting</li><li>Wedding hire</li><li>Alterations</li><li>Gift cards</li><li>Style advice</li></ul>
  </div>
  <div class="abs foot-col" style="left:620px">
    <h4>CUSTOMER HELP</h4>
    <ul><li>FAQ</li><li>Size guide</li><li>Delivery info</li><li>Returns</li><li>Payment options</li><li>Privacy policy</li></ul>
  </div>
  <div class="abs newsletter"><span>Enter your email</span><b></b></div>
  <div class="abs copyright">All rights reserved quillora.com.au</div>
</footer>

</body>
</html>
```